new letterhead/envelope/business card design for law firm

please see attached pdf of current letterhead, envelope and business card. I am also attaching my new logo that I would like to be used. basically, I am looking to refresh and simplify my letterhead/stationary and business card, keeping the following in mind:

overall, I am going for the following look:

-simple,
-modern,
-classy,
-professional

Target Market(s)

law firm clients

Industry/Entity Type

Law Firm

Contact Information for Business Card

see attachment

Font styles to use
Sans Serif

Requirements
Must have
• overall, I am going for the following look:
• -simple,
• -modern,
• -classy,
• -professional
Nice to have
• same as above
Should not have
• no serif fonts

```html
<!DOCTYPE html>
<html lang="en">
<head>
<meta charset="utf-8">
<title>Hollis Law – Letterhead</title>
<link rel="stylesheet" href="https://fonts.googleapis.com/css2?family=Mulish:wght@400;600;700;800&display=swap">
<style>
  :root {
    --backdrop: #d9d9d9;
    --paper: #f6f6f6;
    --navy: #1c2a4e;
    --green: #1f5a34;
    --ink: #4a4a4a;
  }
  * { box-sizing: border-box; margin: 0; padding: 0; }
  html, body {
    width: 1200px; height: 780px; overflow: hidden;
    background: var(--backdrop);
    font-family: "Mulish", sans-serif;
  }
  .canvas {
    width: 1200px; height: 780px;
    display: flex; align-items: center; justify-content: center;
  }
  .letterhead {
    position: relative;
    width: 523px; height: 740px;
    background: var(--paper);
  }
  .brand {
    position: absolute; left: 60px; top: 48px;
    display: flex; flex-direction: column; align-items: center; gap: 10px;
  }
  .brand-dot {
    width: 40px; height: 40px; border-radius: 50%;
    background: var(--green);
  }
  .brand-name {
    color: var(--navy); font-weight: 800;
    font-size: 20px; letter-spacing: 1.5px; line-height: 1;
  }
  .footer {
    position: absolute; left: 35px; right: 31px; bottom: 24px;
    display: flex; align-items: flex-end;
    font-size: 7px; line-height: 10px; color: var(--ink);
  }
  .attorney { width: 123px; }
  .attorney-name { color: var(--green); font-weight: 800; }
  .contact { flex: 1; }
  .contact-line { display: flex; align-items: center; gap: 4px; }
  .contact-line svg { width: 6px; height: 6px; fill: var(--green); }
  .website {
    color: var(--navy); font-weight: 600; letter-spacing: 1px;
    padding-bottom: 1px;
  }
</style>
</head>
<body>
<main class="canvas">
  <section class="letterhead">
    <header class="brand">
      <span class="brand-dot"></span>
      <span class="brand-name">HOLLIS LAW</span>
    </header>

    <footer class="footer">
      <div class="attorney">
        <div class="attorney-name">DANIEL R. HOLLIS, ESQ.</div>
        <div>Licensed in NC and FL</div>
        <div>Board Certified in Civil Trial Law</div>
        <div>by CTAB</div>
      </div>
      <div class="contact">
        <div>2240 Ridgeline Avenue, Suite 410</div>
        <div>Cary, NC 27513</div>
        <div class="contact-line">
          <svg viewBox="0 0 10 10" aria-hidden="true"><path d="M2 0.5 L3.8 2.6 L2.9 3.8 C3.6 5.3 4.7 6.4 6.2 7.1 L7.4 6.2 L9.5 8 L8.4 9.5 C4.2 9.2 0.8 5.8 0.5 1.6 Z"/></svg>
          <span>919.555.0142</span>
        </div>
        <div class="contact-line">
          <svg viewBox="0 0 10 10" aria-hidden="true"><rect x="2.5" y="0.5" width="5" height="2.5"/><rect x="0.5" y="3.5" width="9" height="4"/><rect x="2.5" y="6.5" width="5" height="3"/></svg>
          <span>919.555.0187</span>
        </div>
      </div>
      <div class="website">www.hollislawpa.com</div>
    </footer>
  </section>
</main>
</body>
</html>
```